Vibrational sessions for Healing

I am looking for a business card that is unique that sends a message to open minded folk that vibrational healing is paramount to their life journey and if they are open to this idea it can move mountains for them! All they have to have is a belief! IT is as simple as that!
Willow Harbour is the company based in Western Australia, and as the energy that we are working with is everywhere, it is universal, so to speak!
The design we would like to see is of light shades of rainbow colours radiating light and energy so whatever you think is appropriate to send the message that if you want to move on in you life in a down to earth fashion, then this is the way for folk to find themselves! Something completely different and out of the ordinary and affordable to most, quirky in nature, but completely out of this world idea that will hit the masses by storm!
A website is being developed as we speak, so a new method of healing will be upon us very soon in an unusual fasion, so to speak!
Looking forward to your wonderful bright ideas so we an get started on this venture to enlighten many folk that are on the brink of making a truthful life for themselves.
Warm Regards,
Rosa

Reason: Hi there, I am new to this game and as this is my first time advertising with SketchHive, I was unaware of the time it takes to submit replies and answers to the designers. As I posted the add early in the week, I feel that those first 2 days were just acknowledging designers and sending off extra information for the deign of the card. I would appreciate an extension of time. Thank you. Rosa

Industry/Entity Type

Business

Contact Information for Business Card

Vibrational Healing, Rosa Tindall, Ferncliff WA 6174, Practitioner

Logo styles of interest
Abstract Logo
Requirements
Nice to have
• As this is energy we are talking about, a design that is wispy with a hint of something happening on the card, pastel shades but can be a bold colour somewhere to be a feature but not to striking. Also a vague hint of a clothed body (male or female or both, in dress or suit whatever, casual is fine, in an abstract form) that is just distinguishable in the background.
I would like a design that makes people look twice at the design and then they can read into what can actually happen for themselves.
I hope all this makes sense. Any questions, please email me for clarification.Thank you all for being part of the project to get this underway! This will happen!

```html
<!DOCTYPE html>
<html lang="en">
<head>
<meta charset="utf-8">
<title>Willow Harbour – Vibrational Healing</title>
<link rel="stylesheet" href="https://fonts.googleapis.com/css2?family=EB+Garamond:wght@700&display=swap">
<style>
  :root {
    --ink: #ffffff;
    --magenta: #e0248a;
    --red: #e8402c;
    --orange: #f07a1a;
    --yellow: #e2c224;
    --green: #86b630;
    --teal: #2c8a5c;
    --blue: #1e5c8a;
    --violet: #3a2a7a;
  }
  html, body {
    margin: 0;
    padding: 0;
    width: 1200px;
    height: 693px;
    overflow: hidden;
    background: #ffffff;
  }
  .business-card {
    position: relative;
    width: 1200px;
    height: 693px;
    overflow: hidden;
    background:
      radial-gradient(circle at -6% 6%,
        var(--magenta) 0%,
        var(--red) 22%,
        var(--orange) 36%,
        var(--yellow) 52%,
        var(--green) 63%,
        var(--teal) 75%,
        var(--blue) 86%,
        var(--violet) 100%);
    font-family: "EB Garamond", Garamond, Georgia, serif;
    font-weight: 700;
    color: var(--ink);
  }
  .figure-silhouette {
    position: absolute;
    left: 0;
    top: 0;
    width: 106px;
    height: 693px;
  }
  .line {
    position: absolute;
    left: 0;
    width: 1200px;
    margin: 0;
    text-align: center;
    line-height: 1;
    white-space: nowrap;
    font-weight: 700;
  }
  .company-name    { top: 22px;  font-size: 112px; }
  .company-tagline { top: 115px; font-size: 54px; }
  .person-name     { top: 240px; font-size: 66px; }
  .person-role     { top: 292px; font-size: 52px; }
  .contact         { font-size: 53px; }
  .contact-mobile   { top: 419px; }
  .contact-web      { top: 477px; }
  .contact-email    { top: 534px; }
  .contact-location { top: 601px; }
</style>
</head>
<body>
  <main class="business-card">
    <svg class="figure-silhouette" role="img" aria-label="Faint outline of a standing human figure in profile" viewBox="0 0 106 693" preserveAspectRatio="none">
      <defs>
        <linearGradient id="figureTone" x1="0" y1="0" x2="0" y2="1">
          <stop offset="0" stop-color="#e0248a" stop-opacity="0.35"/>
          <stop offset="0.5" stop-color="#e8402c" stop-opacity="0.3"/>
          <stop offset="1" stop-color="#f07a1a" stop-opacity="0.3"/>
        </linearGradient>
      </defs>
      <rect x="0" y="0" width="106" height="693" fill="url(#figureTone)"/>
    </svg>

    <h1 class="line company-name">Willow Harbour</h1>
    <p class="line company-tagline">Vibrational Healing</p>

    <p class="line person-name">Rosa Tindall</p>
    <p class="line person-role">Practitioner</p>

    <p class="line contact contact-mobile">Mobile: 0412555318</p>
    <p class="line contact contact-web">Web: www.willowharbour.net.au</p>
    <p class="line contact contact-email">Email: Rosa@ willowharbour.net.au</p>
    <p class="line contact contact-location">Located in Ferncliff WA 6174</p>
  </main>
</body>
</html>
```